RKD Cattleworks needs Buisness Card design using new logo

We need a business card design that ties our website and our new logo together. www.rkdcattleworks-example.com The logo will be added to our website at a later date and replace the existing rkd cattleworks that is on the webpage. We are looking for a simple & professional design.

Target Market(s)

Cattle Producers, Ranchers

Industry/Entity Type

Agriculture

Contact Information for Business Card

Side one:
logo
www.rkdcattleworks-example.com

Side two:
RKD Cattleworks
Dennis & Marla Kovacs
Willowmere, MB Canada
(555) 316-2984/(555) 472-9051
kovacs47@ploverline-example.net

Font styles to use
Serif
Sans Serif
Script

Requirements
Must have
• We would like to tie our new logo in with our website on the business card.

```html
<!DOCTYPE html>
<html lang="en">
<head>
<meta charset="utf-8">
<title>RKD Cattleworks — Business Card</title>
<link rel="stylesheet" href="https://fonts.googleapis.com/css2?family=Lato:wght@400;700&display=swap">
<style>
  :root {
    --backdrop: #e4e4e6;
    --card: #f7f7f7;
    --ink: #333336;
    --band: #3a3a3c;
    --accent: #d9232b;
    --rule: #9a9a9a;
    --shadow: rgba(0, 0, 0, 0.18);
  }
  * { box-sizing: border-box; margin: 0; padding: 0; }
  html, body {
    width: 1200px;
    height: 913px;
    overflow: hidden;
    background: var(--backdrop);
    font-family: "Lato", Arial, sans-serif;
    color: var(--ink);
  }
  .sheet {
    position: relative;
    width: 1200px;
    height: 913px;
  }
  .card {
    position: absolute;
    top: 168px;
    width: 330px;
    height: 576px;
    background: var(--card);
    box-shadow: 0 10px 28px var(--shadow);
    overflow: hidden;
  }
  .card--back { left: 215px; }
  .card--front { left: 655px; }

  /* Back side */
  .band {
    position: absolute;
    left: 190px;
    width: 58px;
    background: var(--band);
  }
  .band--top { top: 0; height: 86px; }
  .band--bottom { top: 196px; height: 300px; left: 82px; }
  .wordmark {
    font-weight: 400;
    color: var(--ink);
    text-align: center;
    letter-spacing: 0.5px;
    line-height: 1.1;
  }
  .card--back .wordmark {
    position: absolute;
    top: 110px;
    left: 0;
    right: 0;
    font-size: 34px;
  }
  .website {
    position: absolute;
    bottom: 36px;
    right: 28px;
    font-size: 14px;
    font-weight: 700;
    color: var(--ink);
  }
  .website .domain { color: var(--accent); }

  /* Front side */
  .card--front .wordmark {
    margin-top: 108px;
    font-size: 34px;
  }
  .names {
    margin-top: 34px;
    text-align: center;
    font-size: 13px;
    font-weight: 700;
    letter-spacing: 0.4px;
    text-transform: uppercase;
    color: var(--accent);
  }
  .location {
    margin: 26px 34px 0;
    padding: 9px 0;
    border-top: 1.5px dashed var(--rule);
    border-bottom: 1.5px dashed var(--rule);
  }
  .contact-list {
    list-style: none;
    margin: 24px 34px 0;
  }
  .contact-row {
    display: flex;
    align-items: center;
    gap: 10px;
    font-size: 14px;
    line-height: 1.9;
  }
  .location.contact-row { line-height: 1.5; }
  .icon {
    flex: 0 0 auto;
    width: 15px;
    height: 15px;
  }
</style>
</head>
<body>
<main class="sheet">

  <section class="card card--back" aria-label="Business card, logo side">
    <div class="band band--top"></div>
    <p class="wordmark">RKD Cattleworks</p>
    <div class="band band--bottom"></div>
    <p class="website">www.<span class="domain">rkdcattleworks-example</span>.com</p>
  </section>

  <section class="card card--front" aria-label="Business card, contact side">
    <p class="wordmark">RKD Cattleworks</p>
    <p class="names">Dennis &amp; Marla Kovacs</p>

    <p class="location contact-row">
      <svg class="icon" viewBox="0 0 16 16" aria-hidden="true">
        <circle cx="8" cy="8" r="8" fill="var(--accent)"/>
        <path d="M8 3.6a2.9 2.9 0 0 0-2.9 2.9C5.1 8.7 8 12.3 8 12.3s2.9-3.6 2.9-5.8A2.9 2.9 0 0 0 8 3.6z" fill="#fff"/>
        <circle cx="8" cy="6.5" r="1.1" fill="var(--accent)"/>
      </svg>
      Willowmere, MB Canada
    </p>

    <ul class="contact-list">
      <li class="contact-row">
        <svg class="icon" viewBox="0 0 16 16" aria-hidden="true">
          <circle cx="8" cy="8" r="8" fill="var(--accent)"/>
          <path d="M5.2 4.2l1.4-.4 1 2.1-.9.8c.4.9 1.1 1.6 2 2l.8-.9 2.1 1-.4 1.4c-3 .3-6.3-3-6-6z" fill="#fff"/>
        </svg>
        (555) 316-2984
      </li>
      <li class="contact-row">
        <svg class="icon" viewBox="0 0 16 16" aria-hidden="true">
          <circle cx="8" cy="8" r="8" fill="var(--accent)"/>
          <rect x="5.5" y="3.6" width="5" height="8.8" rx="1" fill="#fff"/>
          <rect x="6.3" y="4.7" width="3.4" height="5.6" fill="var(--accent)"/>
        </svg>
        (555) 472-9051
      </li>
      <li class="contact-row">
        <svg class="icon" viewBox="0 0 16 16" aria-hidden="true">
          <circle cx="8" cy="8" r="8" fill="var(--accent)"/>
          <rect x="4" y="5.2" width="8" height="5.6" rx="0.6" fill="#fff"/>
          <path d="M4.3 5.6L8 8.4l3.7-2.8" fill="none" stroke="var(--accent)" stroke-width="0.9"/>
        </svg>
        kovacs47@ploverline-example.net
      </li>
    </ul>
  </section>

</main>
</body>
</html>
```